Business Card Design Project

I want my business cards to stand and feel timeless! I also want people to get their hands on them and freak out over how cool these are, I already have a logo i just want a very cool card design! this is for a makeup artist and maybe one day a line of cosmetics.

Target Market(s)

I want this to target women from 18 to 45

Industry/Entity Type

Business

Font styles to use
Decorative
Script

Colors

Designer to choose colors to be used in the design.

Requirements
Must have
• it must be elegante

```html
<!DOCTYPE html>
<html lang="en">
<head>
<meta charset="utf-8">
<title>Clara Rose – Business Card</title>
<link rel="stylesheet" href="https://fonts.googleapis.com/css2?family=Cinzel:wght@400&family=Crimson+Text&display=swap">
<style>
  :root {
    --page: #ffffff;
    --gold-light: #fbf0a8;
    --gold-mid: #f3d98a;
    --gold-deep: #e2b95a;
    --band-light: #f6d98a;
    --band-dark: #d9a54a;
    --band-edge: #8a5a1c;
    --ink-dark: #1e1a14;
    --ink-brown: #6b3e13;
  }
  * { margin: 0; padding: 0; box-sizing: border-box; }
  html, body {
    width: 1200px;
    height: 375px;
    overflow: hidden;
    background: var(--page);
  }
  .sheet {
    position: relative;
    width: 1200px;
    height: 375px;
  }
  .card {
    position: absolute;
    top: 33px;
    width: 543px;
    height: 310px;
    overflow: hidden;
  }
  .card--front {
    left: 39px;
    background: radial-gradient(ellipse at 50% 55%, var(--gold-light) 0%, var(--gold-light) 35%, var(--gold-mid) 75%, var(--gold-deep) 100%);
    display: flex;
    align-items: center;
    justify-content: center;
  }
  .brand-name {
    font-family: "Cinzel", serif;
    font-weight: 400;
    font-size: 40px;
    letter-spacing: 6px;
    color: var(--ink-dark);
    margin-top: 8px;
  }
  .card--back {
    left: 613px;
  }
  .damask-field {
    position: absolute;
    inset: 0;
    background: radial-gradient(ellipse at 50% 50%, var(--gold-light) 0%, var(--gold-mid) 55%, var(--gold-deep) 100%);
  }
  .title-band {
    position: absolute;
    left: 0;
    top: 122px;
    width: 100%;
    height: 67px;
    background: linear-gradient(to bottom, var(--band-dark) 0%, var(--band-light) 35%, var(--band-light) 60%, var(--band-dark) 100%);
    border-top: 1px solid var(--band-edge);
    border-bottom: 3px solid var(--band-edge);
    text-align: center;
    color: var(--ink-brown);
    font-family: "Cinzel", serif;
  }
  .title-band__name {
    font-size: 27px;
    letter-spacing: 1px;
    line-height: 1;
    margin-top: 8px;
  }
  .title-band__role {
    font-size: 16px;
    letter-spacing: 0.5px;
    margin-top: 4px;
  }
  .contact-line {
    position: absolute;
    left: 0;
    bottom: 12px;
    width: 100%;
    text-align: center;
    font-family: "Crimson Text", serif;
    font-size: 15px;
    color: var(--ink-brown);
  }
</style>
</head>
<body>
  <main class="sheet">
    <section class="card card--front">
      <div class="brand-name">CLARA ROSE</div>
    </section>

    <section class="card card--back">
      <div class="damask-field" role="img" aria-label="Gold damask ornament pattern"></div>
      <div class="title-band">
        <div class="title-band__name">Clara Rose</div>
        <div class="title-band__role">Make-Up Artist</div>
      </div>
      <p class="contact-line">Email: clararose@example.com | Tel: +000 .000.0000</p>
    </section>
  </main>
</body>
</html>
```